Wiggle Wave - A physical literacy program for daycare centers

A brochure that shows parents what our program is all about. I've created a mock up of the brochure and would ask that the designer follows this for the initial design.

```html
<!DOCTYPE html>
<html lang="en">
<head>
<meta charset="utf-8">
<title>Wiggle Wave – Brochure Spreads</title>
<link rel="stylesheet" href="https://fonts.googleapis.com/css2?family=Poppins:ital,wght@0,300;0,700;0,800;1,700&family=Open+Sans:ital,wght@1,400&display=swap">
<style>
  :root {
    --canvas: #eef1f2;
    --paper: #ffffff;
    --navy: #27338f;
    --green: #3cb043;
    --pink: #e5157f;
    --purple: #8e2a9c;
    --orange: #ee5a24;
    --red: #e2232a;
    --sky: #2b8fcb;
    --grey-text: #6e6e6e;
    --dot-navy: #2a3596;
  }
  * { margin: 0; padding: 0; box-sizing: border-box; }
  html, body { width: 1014px; height: 1200px; overflow: hidden; }
  body {
    background: var(--canvas);
    display: flex;
    flex-direction: column;
    align-items: center;
    justify-content: center;
    gap: 18px;
    font-family: "Poppins", sans-serif;
  }
  .spread {
    width: 740px;
    height: 573px;
    display: block;
    background: var(--paper);
    box-shadow: 0 4px 14px rgba(0,0,0,0.18);
  }
  .placeholder-copy { font-family: "Poppins", sans-serif; font-weight: 300; font-size: 23px; fill: var(--grey-text); letter-spacing: 0.5px; }
  .headline { font-family: "Poppins", sans-serif; font-weight: 700; font-size: 22px; }
  .headline--green { fill: var(--green); }
  .headline--purple { fill: var(--purple); }
  .brand-name { font-family: "Poppins", sans-serif; font-weight: 800; fill: var(--navy); }
  .brand-tagline { font-family: "Open Sans", sans-serif; font-style: italic; font-size: 16px; fill: var(--sky); }
  .promise { font-family: "Poppins", sans-serif; font-style: italic; font-weight: 700; font-size: 19px; fill: var(--navy); }
  .ring { fill: none; stroke-width: 3; }
</style>
</head>
<body>

<!-- Outer spread: cover, advantage panel, back panel -->
<svg class="spread spread--outer" viewBox="0 0 788 610" xmlns="http://www.w3.org/2000/svg">
  <defs>
    <linearGradient id="gym-warm" x1="0" y1="0" x2="0" y2="1">
      <stop offset="0" stop-color="#b08a5c"/><stop offset="0.6" stop-color="#c9a13a"/><stop offset="1" stop-color="#d8c21f"/>
    </linearGradient>
    <linearGradient id="gym-mat" x1="0" y1="0" x2="0" y2="1">
      <stop offset="0" stop-color="#c8b49a"/><stop offset="0.55" stop-color="#2f3f8c"/><stop offset="1" stop-color="#c83030"/>
    </linearGradient>
    <linearGradient id="gym-dark" x1="0" y1="0" x2="1" y2="1">
      <stop offset="0" stop-color="#3a3e7a"/><stop offset="0.5" stop-color="#c7a27c"/><stop offset="1" stop-color="#2a2a2a"/>
    </linearGradient>
    <linearGradient id="gear-teal" x1="0" y1="0" x2="0" y2="1">
      <stop offset="0" stop-color="#a6dccf"/><stop offset="0.6" stop-color="#e55a9a"/><stop offset="1" stop-color="#2f2f33"/>
    </linearGradient>
    <linearGradient id="floor-grey" x1="0" y1="0" x2="0" y2="1">
      <stop offset="0" stop-color="#d9d9d9"/><stop offset="0.6" stop-color="#c04040"/><stop offset="1" stop-color="#8a8a8a"/>
    </linearGradient>
    <linearGradient id="child-red" x1="0" y1="0" x2="0" y2="1">
      <stop offset="0" stop-color="#c9b48e"/><stop offset="1" stop-color="#a8322c"/>
    </linearGradient>
  </defs>

  <rect width="788" height="610" fill="var(--paper)"/>

  <circle class="decor-arc" cx="-85" cy="320" r="103" fill="var(--purple)"/>
  <circle class="decor-dot" cx="179" cy="417" r="10" fill="var(--dot-navy)"/>

  <g class="photo photo--handstand">
    <circle cx="84" cy="87" r="88" fill="url(#gym-warm)" role="img" aria-label="Photo of a child doing a handstand on a yellow mat"/>
    <circle class="ring" cx="84" cy="87" r="96" stroke="var(--green)"/>
  </g>

  <text class="placeholder-copy" text-anchor="middle">
    <tspan x="228" y="210">YOUR</tspan><tspan x="228" y="238">TEXT</tspan><tspan x="228" y="266">GOES</tspan><tspan x="228" y="294">HERE</tspan>
  </text>

  <text class="headline headline--green" text-anchor="middle">
    <tspan x="392" y="42">The Wiggle Wave</tspan><tspan x="392" y="67">Advantage</tspan>
  </text>

  <g class="brand">
    <circle cx="582" cy="66" r="20" fill="var(--green)"/>
    <text class="brand-name"><tspan x="612" y="55" font-size="30">Wiggle</tspan><tspan x="612" y="90" font-size="34">Wave</tspan></text>
    <text class="brand-tagline" x="660" y="113" text-anchor="middle">Bringing our gym to you</text>
  </g>

  <g class="photo photo--stretch">
    <circle cx="493" cy="194" r="88" fill="url(#gym-mat)" role="img" aria-label="Photo of a girl stretching on a gym mat"/>
    <circle class="ring" cx="493" cy="194" r="96" stroke="var(--pink)"/>
  </g>

  <g class="photo photo--bar">
    <circle cx="670" cy="272" r="118" fill="url(#gym-dark)" role="img" aria-label="Photo of a coach helping a child hang from a bar"/>
    <circle class="ring" cx="670" cy="272" r="127" stroke="var(--navy)"/>
  </g>

  <g class="photo photo--equipment-floor">
    <circle cx="115" cy="527" r="88" fill="url(#floor-grey)" role="img" aria-label="Photo of soft gym blocks and mats on the floor"/>
    <circle class="ring" cx="115" cy="527" r="96" stroke="var(--orange)"/>
  </g>

  <g class="photo photo--gear">
    <circle cx="370" cy="497" r="158" fill="url(#gear-teal)" role="img" aria-label="Photo of an exercise ball, mat, step and jump rope"/>
    <circle class="ring" cx="370" cy="497" r="166" stroke="var(--red)"/>
  </g>

  <g class="photo photo--crawl">
    <circle cx="605" cy="572" r="73" fill="url(#child-red)" role="img" aria-label="Photo of a boy crawling on the floor"/>
    <circle class="ring" cx="605" cy="572" r="81" stroke="var(--purple)"/>
  </g>

  <text class="headline headline--purple" text-anchor="end">
    <tspan x="771" y="446">A physical literacy</tspan><tspan x="771" y="470">program for</tspan><tspan x="771" y="494">daycare</tspan><tspan x="771" y="518">center</tspan>
  </text>
</svg>

<!-- Inner spread: three inside panels -->
<svg class="spread spread--inner" viewBox="0 0 788 610" xmlns="http://www.w3.org/2000/svg">
  <defs>
    <linearGradient id="in-warm" x1="0" y1="0" x2="0" y2="1">
      <stop offset="0" stop-color="#b5865a"/><stop offset="0.7" stop-color="#e0dcd8"/><stop offset="1" stop-color="#c8232e"/>
    </linearGradient>
    <linearGradient id="in-class" x1="0" y1="0" x2="0" y2="1">
      <stop offset="0" stop-color="#6c6a7a"/><stop offset="0.55" stop-color="#8c8aa6"/><stop offset="1" stop-color="#d8b21c"/>
    </linearGradient>
    <linearGradient id="in-coach" x1="0" y1="0" x2="1" y2="1">
      <stop offset="0" stop-color="#d8b88a"/><stop offset="0.5" stop-color="#4a5a3a"/><stop offset="1" stop-color="#d8b51c"/>
    </linearGradient>
    <linearGradient id="in-bend" x1="0" y1="0" x2="0" y2="1">
      <stop offset="0" stop-color="#c9a24a"/><stop offset="0.6" stop-color="#e9e6e2"/><stop offset="1" stop-color="#2b3f8f"/>
    </linearGradient>
    <linearGradient id="in-lunge" x1="0" y1="0" x2="0" y2="1">
      <stop offset="0" stop-color="#3f6ab0"/><stop offset="0.6" stop-color="#9aa0b8"/><stop offset="1" stop-color="#d7b51f"/>
    </linearGradient>
  </defs>

  <rect width="788" height="610" fill="var(--paper)"/>

  <circle class="decor-arc" cx="349" cy="-12" r="45" fill="var(--green)"/>
  <circle class="decor-dot" cx="409" cy="24" r="7" fill="var(--dot-navy)"/>
  <circle class="decor-arc" cx="880" cy="267" r="105" fill="var(--purple)"/>
  <circle class="decor-dot" cx="584" cy="577" r="10" fill="var(--orange)"/>

  <g class="brand">
    <circle cx="56" cy="66" r="20" fill="var(--green)"/>
    <text class="brand-name"><tspan x="86" y="55" font-size="30">Wiggle</tspan><tspan x="86" y="90" font-size="34">Wave</tspan></text>
    <text class="brand-tagline" x="134" y="113" text-anchor="middle">Bringing our gym to you</text>
  </g>

  <g class="photo photo--pike">
    <circle cx="627" cy="67" r="77" fill="url(#in-bend)" role="img" aria-label="Photo of a child bending forward on a mat"/>
    <circle class="ring" cx="627" cy="67" r="85" stroke="var(--pink)"/>
  </g>

  <g class="photo photo--class">
    <circle cx="189" cy="387" r="142" fill="url(#in-class)" role="img" aria-label="Photo of children exercising together in a gym class"/>
    <circle class="ring" cx="189" cy="387" r="150" stroke="var(--green)"/>
  </g>

  <g class="photo photo--star">
    <circle cx="114" cy="227" r="87" fill="url(#in-warm)" role="img" aria-label="Photo of a smiling girl with arms outstretched on a red mat"/>
    <circle class="ring" cx="114" cy="227" r="95" stroke="var(--purple)"/>
  </g>

  <g class="photo photo--coach">
    <circle cx="406" cy="212" r="92" fill="url(#in-coach)" role="img" aria-label="Photo of a coach lifting a child on a bar"/>
    <circle class="ring" cx="406" cy="212" r="100" stroke="var(--orange)"/>
  </g>

  <g class="photo photo--lunge">
    <circle cx="694" cy="512" r="87" fill="url(#in-lunge)" role="img" aria-label="Photo of a toddler doing a wide lunge on a mat"/>
    <circle class="ring" cx="694" cy="512" r="95" stroke="var(--navy)"/>
  </g>

  <text class="placeholder-copy" text-anchor="middle">
    <tspan x="661" y="237">YOUR</tspan><tspan x="661" y="265">TEXT</tspan><tspan x="661" y="293">GOES</tspan><tspan x="661" y="321">HERE</tspan>
  </text>
  <text class="placeholder-copy" text-anchor="middle">
    <tspan x="429" y="400">YOUR</tspan><tspan x="429" y="428">TEXT</tspan><tspan x="429" y="456">GOES</tspan><tspan x="429" y="484">HERE</tspan>
  </text>

  <text class="promise">
    <tspan x="20" y="570">We help your child develop exercies</tspan><tspan x="18" y="593">habits and skills for life</tspan>
  </text>
</svg>

</body>
</html>
```